Fresh new and cool frozen burger box! Come be a part of an amazing project!

Ember Lane Kitchen Co restaurant is expanding into the frozen foods market!
please check out our website to understand the vibe of the company
https://quillfare.ca
this is a line of premium Halal meat, we want to stress our top-notch quality.
we like the orange colours so see what you can do with them. (maybe white and orange combo)
you have lots of creative freedom here, feel free to use the burger photo I am attaching or any image off the website.
logo should be nice and visible.
we want this packaging to really stand out and be special.
Come be a part of an amazing project!
Muslim Flails, looking of a quality meat burger. mostly already familiar with our brand
Frozen food

```html
<!DOCTYPE html>
<html lang="en">
<head>
<meta charset="utf-8">
<title>Ember Lane Kitchen Co – Premium Frozen Burger Box Dieline</title>
<link rel="stylesheet" href="https://fonts.googleapis.com/css2?family=Passion+One:wght@400;700&family=Oswald:wght@700&family=Open+Sans:wght@600;700;800&display=swap">
<style>
  :root {
    --orange: #f39a2d;
    --orange-deep: #e88a17;
    --wood-dark: #1d1d1f;
    --wood-mid: #2e2e31;
    --white: #ffffff;
    --paper: #ffffff;
    --bun-light: #eaa656;
    --bun-dark: #b8662c;
    --head: "Passion One", "Arial Black", sans-serif;
    --name: "Oswald", "Arial Narrow", sans-serif;
    --body: "Open Sans", Arial, sans-serif;
  }
  * { box-sizing: border-box; margin: 0; padding: 0; }
  html, body { width: 1010px; height: 1200px; overflow: hidden; background: var(--paper); }
  .canvas { position: relative; width: 1010px; height: 1200px; }

  .dieline-shapes { position: absolute; left: 0; top: 0; }

  .panel { position: absolute; overflow: hidden; }
  .panel--front { width: 475px; height: 270px; left: 267px; }
  .panel--front.is-first { top: 330px; }
  .panel--front.is-second { top: 775px; }
  .panel--lid { width: 475px; height: 175px; left: 267px; transform: rotate(180deg); }
  .panel--lid.is-top { top: 155px; }
  .panel--lid.is-bottom { top: 600px; }

  .panel__ground { position: absolute; inset: 0; }
  .photo {
    position: absolute;
    border-radius: 10px;
    background: linear-gradient(180deg, var(--bun-light) 0%, var(--bun-dark) 100%);
  }

  .abs { position: absolute; white-space: nowrap; }

  .brand__dot { width: 18px; height: 18px; border-radius: 50%; border: 2px solid var(--white); background: var(--orange-deep); }
  .brand__name { font-family: var(--name); font-weight: 700; color: var(--orange); font-size: 19px; line-height: 19px; letter-spacing: 0.5px; text-transform: uppercase; }
  .brand__line { font-family: var(--body); font-weight: 700; color: var(--white); font-size: 14px; }

  .premium-band { background: var(--orange-deep); clip-path: polygon(3% 10%, 100% 0, 97% 90%, 0 100%); }
  .premium-text { font-family: var(--head); font-weight: 700; color: #ffd08a; font-size: 16px; letter-spacing: 0.5px; }

  .title { font-family: var(--head); font-weight: 700; font-size: 44px; line-height: 38px; letter-spacing: 1px; }
  .title--white { color: var(--white); }
  .title--orange { color: var(--orange); }

  .rule { height: 3px; background: var(--white); border-radius: 2px; opacity: 0.9; }

  .social { display: flex; align-items: center; gap: 4px; }
  .social__dot { width: 14px; height: 14px; border-radius: 50%; border: 1.5px solid var(--orange); }
  .social__url { font-family: var(--body); font-weight: 700; color: var(--orange); font-size: 11px; margin-left: 4px; }

  .count-ring { width: 82px; height: 82px; border-radius: 50%; border: 3px solid var(--white); display: flex; align-items: center; justify-content: center; }
  .count-ring__num { font-family: var(--head); font-weight: 700; color: var(--orange); font-size: 72px; line-height: 1; margin-top: 6px; }

  .ingredients-title { font-family: var(--head); font-weight: 700; color: var(--orange); font-size: 18px; }
  .ingredients-list { list-style: none; font-family: var(--body); font-weight: 700; color: var(--white); font-size: 6px; line-height: 8px; }
  .ingredients-list li::before { content: ""; display: inline-block; width: 4px; height: 4px; border-radius: 50%; background: var(--orange); margin-right: 3px; }
  .fine { font-family: var(--body); font-weight: 800; color: var(--white); font-size: 5.5px; line-height: 7px; text-align: center; }
  .claim { font-family: var(--head); font-weight: 700; color: var(--white); font-size: 15px; }
  .pack-count { font-family: var(--head); font-weight: 700; color: var(--orange); font-size: 26px; line-height: 1; }

  .end-flap { position: absolute; top: 0; left: 0; width: 270px; height: 245px; display: flex; flex-direction: column; align-items: center; justify-content: center; gap: 6px; }
  .end-flap__name { font-family: var(--name); font-weight: 700; color: var(--white); font-size: 21px; line-height: 1; letter-spacing: 0.5px; text-transform: uppercase; white-space: nowrap; }
  .end-flap__tag { font-family: var(--body); font-weight: 600; color: var(--white); font-size: 12px; letter-spacing: 1px; white-space: nowrap; }
  .end-flap-holder { position: absolute; width: 245px; height: 270px; }
  .end-flap-holder.is-left { left: 22px; top: 330px; }
  .end-flap-holder.is-right { left: 742px; top: 775px; }
  .end-flap-holder.is-left .end-flap { transform: translate(245px, 0) rotate(90deg); transform-origin: 0 0; }
  .end-flap-holder.is-right .end-flap { transform: translate(0, 270px) rotate(-90deg); transform-origin: 0 0; }
</style>
</head>
<body>
<main class="canvas">

  <svg class="dieline-shapes" width="1010" height="1200" viewBox="0 0 1010 1200" aria-hidden="true">
    <defs>
      <linearGradient id="wood" x1="0" y1="0" x2="1" y2="1">
        <stop offset="0" stop-color="#333336"/>
        <stop offset="0.5" stop-color="#1f1f21"/>
        <stop offset="1" stop-color="#2b2b2e"/>
      </linearGradient>
    </defs>
    <polygon points="142,172 250,172 267,160 267,325 250,315 142,315" fill="var(--orange)"/>
    <polygon points="742,160 759,172 867,172 867,315 759,315 742,325" fill="var(--orange)"/>
    <polygon points="142,617 250,617 267,605 267,770 250,760 142,760" fill="var(--orange)"/>
    <polygon points="742,605 759,617 867,617 867,760 759,760 742,770" fill="var(--orange)"/>
    <path d="M267,330 H62 Q22,330 22,370 V560 Q22,600 62,600 H267 Z" fill="url(#wood)"/>
    <path d="M742,775 H947 Q987,775 987,815 V1005 Q987,1045 947,1045 H742 Z" fill="url(#wood)"/>
  </svg>

  <!-- Lid panel (printed upside down) -->
  <section class="panel panel--lid is-top">
    <svg class="panel__ground" width="475" height="175" viewBox="0 0 475 175" aria-hidden="true">
      <rect width="475" height="175" fill="var(--orange)"/>
      <path d="M0,0 H320 Q250,90 300,175 H0 Z" fill="url(#woodLid)"/>
      <defs><linearGradient id="woodLid" x1="0" y1="0" x2="1" y2="1"><stop offset="0" stop-color="#333336"/><stop offset="1" stop-color="#1f1f21"/></linearGradient></defs>
    </svg>
    <div class="photo" role="img" aria-label="Photo of a sesame bun burger with bacon, cheese, tomato and lettuce" style="left:300px;top:12px;width:160px;height:150px;"></div>
    <div class="abs premium-band" style="left:40px;top:42px;width:150px;height:17px;"></div>
    <div class="abs premium-text" style="left:70px;top:40px;">PREMIUM</div>
    <div class="abs title title--white" style="left:45px;top:70px;">FROZEN</div>
    <div class="abs title title--orange" style="left:45px;top:108px;">BURGER</div>
    <div class="abs rule" style="left:40px;top:150px;width:160px;"></div>
    <div class="abs social" style="left:55px;top:156px;"><span class="social__dot"></span><span class="social__dot"></span><span class="social__dot"></span><span class="social__url">quillfare.ca</span></div>
  </section>

  <!-- Front panel -->
  <section class="panel panel--front is-first">
    <svg class="panel__ground" width="475" height="270" viewBox="0 0 475 270" aria-hidden="true">
      <rect width="475" height="270" fill="var(--orange)"/>
      <path d="M165,0 H475 V270 H175 Q135,140 165,0 Z" fill="url(#woodFront)"/>
      <defs><linearGradient id="woodFront" x1="0" y1="0" x2="1" y2="1"><stop offset="0" stop-color="#333336"/><stop offset="1" stop-color="#1f1f21"/></linearGradient></defs>
    </svg>
    <div class="photo" role="img" aria-label="Photo of a sesame bun burger with bacon, cheese, tomato and lettuce" style="left:0;top:28px;width:175px;height:218px;border-radius:0 10px 10px 0;"></div>
    <div class="abs brand__dot" style="left:186px;top:40px;"></div>
    <div class="abs brand__name" style="left:212px;top:22px;">Ember Lane<br>Kitchen Co</div>
    <div class="abs brand__line" style="left:215px;top:60px;">Burgers</div>
    <div class="abs premium-band" style="left:195px;top:100px;width:150px;height:17px;"></div>
    <div class="abs premium-text" style="left:215px;top:98px;">PREMIUM</div>
    <div class="abs title title--white" style="left:198px;top:130px;">FROZEN</div>
    <div class="abs title title--orange" style="left:198px;top:170px;">BURGER</div>
    <div class="abs rule" style="left:205px;top:236px;width:140px;"></div>
    <div class="abs social" style="left:210px;top:243px;"><span class="social__dot"></span><span class="social__dot"></span><span class="social__dot"></span><span class="social__url">quillfare.ca</span></div>
    <div class="abs count-ring" style="left:365px;top:30px;"><span class="count-ring__num">3</span></div>
    <div class="abs ingredients-title" style="left:358px;top:116px;">INGREDIENTS</div>
    <ul class="abs ingredients-list" style="left:380px;top:138px;"><li>LOREM IPSUM</li><li>LOREM IPSUM</li><li>LOREM IPSUM</li></ul>
    <div class="abs fine" style="left:365px;top:166px;width:90px;">MADE FROM LOREM IPSUM<br>RAISED WITH</div>
    <div class="abs claim" style="left:366px;top:180px;">LOREM IPSUM</div>
    <div class="abs pack-count" style="left:368px;top:202px;">12</div>
    <div class="abs fine" style="left:390px;top:208px;width:50px;">BURGER POUND<br>BURGERS</div>
    <div class="abs fine" style="left:380px;top:240px;width:70px;">KEEP FROZEN<br>RAW + READY TO COOK</div>
  </section>

  <!-- Base panel (printed upside down) -->
  <section class="panel panel--lid is-bottom">
    <svg class="panel__ground" width="475" height="175" viewBox="0 0 475 175" aria-hidden="true">
      <rect width="475" height="175" fill="var(--orange)"/>
      <path d="M0,0 H320 Q250,90 300,175 H0 Z" fill="url(#woodBase)"/>
      <defs><linearGradient id="woodBase" x1="0" y1="0" x2="1" y2="1"><stop offset="0" stop-color="#333336"/><stop offset="1" stop-color="#1f1f21"/></linearGradient></defs>
    </svg>
    <div class="photo" role="img" aria-label="Photo of a sesame bun burger with bacon, cheese, tomato and lettuce" style="left:300px;top:12px;width:160px;height:150px;"></div>
    <div class="abs premium-band" style="left:40px;top:42px;width:150px;height:17px;"></div>
    <div class="abs premium-text" style="left:70px;top:40px;">PREMIUM</div>
    <div class="abs title title--white" style="left:45px;top:70px;">FROZEN</div>
    <div class="abs title title--orange" style="left:45px;top:108px;">BURGER</div>
    <div class="abs rule" style="left:40px;top:150px;width:160px;"></div>
    <div class="abs social" style="left:55px;top:156px;"><span class="social__dot"></span><span class="social__dot"></span><span class="social__dot"></span><span class="social__url">quillfare.ca</span></div>
  </section>

  <!-- Back panel -->
  <section class="panel panel--front is-second">
    <svg class="panel__ground" width="475" height="270" viewBox="0 0 475 270" aria-hidden="true">
      <rect width="475" height="270" fill="var(--orange)"/>
      <path d="M165,0 H475 V270 H175 Q135,140 165,0 Z" fill="url(#woodBack)"/>
      <defs><linearGradient id="woodBack" x1="0" y1="0" x2="1" y2="1"><stop offset="0" stop-color="#333336"/><stop offset="1" stop-color="#1f1f21"/></linearGradient></defs>
    </svg>
    <div class="photo" role="img" aria-label="Photo of a sesame bun burger with bacon, cheese, tomato and lettuce" style="left:0;top:28px;width:175px;height:218px;border-radius:0 10px 10px 0;"></div>
    <div class="abs brand__dot" style="left:186px;top:40px;"></div>
    <div class="abs brand__name" style="left:212px;top:22px;">Ember Lane<br>Kitchen Co</div>
    <div class="abs brand__line" style="left:215px;top:60px;">Burgers</div>
    <div class="abs premium-band" style="left:195px;top:100px;width:150px;height:17px;"></div>
    <div class="abs premium-text" style="left:215px;top:98px;">PREMIUM</div>
    <div class="abs title title--white" style="left:198px;top:130px;">FROZEN</div>
    <div class="abs title title--orange" style="left:198px;top:170px;">BURGER</div>
    <div class="abs rule" style="left:205px;top:236px;width:140px;"></div>
    <div class="abs social" style="left:210px;top:243px;"><span class="social__dot"></span><span class="social__dot"></span><span class="social__dot"></span><span class="social__url">quillfare.ca</span></div>
    <div class="abs count-ring" style="left:365px;top:30px;"><span class="count-ring__num">3</span></div>
    <div class="abs ingredients-title" style="left:358px;top:116px;">INGREDIENTS</div>
    <ul class="abs ingredients-list" style="left:380px;top:138px;"><li>LOREM IPSUM</li><li>LOREM IPSUM</li><li>LOREM IPSUM</li></ul>
    <div class="abs fine" style="left:365px;top:166px;width:90px;">MADE FROM LOREM IPSUM<br>RAISED WITH</div>
    <div class="abs claim" style="left:366px;top:180px;">LOREM IPSUM</div>
    <div class="abs pack-count" style="left:368px;top:202px;">12</div>
    <div class="abs fine" style="left:390px;top:208px;width:50px;">BURGER POUND<br>BURGERS</div>
    <div class="abs fine" style="left:380px;top:240px;width:70px;">KEEP FROZEN<br>RAW + READY TO COOK</div>
  </section>

  <!-- End flaps -->
  <div class="end-flap-holder is-left">
    <div class="end-flap">
      <div class="end-flap__name">Ember Lane Kitchen Co</div>
      <div class="end-flap__tag">Pizza • Burgers • Wings</div>
    </div>
  </div>
  <div class="end-flap-holder is-right">
    <div class="end-flap">
      <div class="end-flap__name">Ember Lane Kitchen Co</div>
      <div class="end-flap__tag">Pizza • Burgers • Wings</div>
    </div>
  </div>

</main>
</body>
</html>
```